Larchly Business Cards

Create new business cards with the details below.

Trevor Halse
Director

MB: +61 417 352 940
PH: 1300 514 637
Email: trevor.halse@larchly-example.com.au
Address: 27A Pemberly Lane, Brackenvale VIC 3999 Australia
Website: www.larchly-example.com.au

Requirements
Must have
• must be clean looking

```html
<!DOCTYPE html>
<html lang="en">
<head>
<meta charset="utf-8">
<title>Larchly Business Cards</title>
<link href="https://fonts.googleapis.com/css2?family=Roboto:wght@400;500;700&display=swap" rel="stylesheet">
<style>
  :root {
    --bg: #ecebe8;
    --card: #ffffff;
    --lime: #9acb1c;
    --ink: #1e1e1e;
    --muted: #3a3a3a;
  }
  * { box-sizing: border-box; margin: 0; padding: 0; }
  html, body { width: 1200px; height: 913px; overflow: hidden; }
  body {
    background: var(--bg);
    font-family: "Roboto", Arial, sans-serif;
    color: var(--ink);
    position: relative;
  }
  .card {
    position: absolute;
    width: 560px;
    height: 320px;
    background: var(--card);
    box-shadow: 0 6px 18px rgba(0,0,0,0.12);
  }
  .card--front { left: 80px; top: 110px; }
  .card--back { left: 560px; top: 480px; }

  .brand {
    display: flex;
    align-items: center;
    gap: 14px;
  }
  .brand__mark {
    width: 34px; height: 34px;
    background: var(--lime);
  }
  .brand__name {
    font-weight: 700;
    color: var(--lime);
    letter-spacing: 1px;
    text-transform: uppercase;
  }
  .card--front .brand {
    position: absolute;
    left: 0; right: 0; top: 0; bottom: 0;
    justify-content: center;
  }
  .card--front .brand__name { font-size: 62px; }

  .card--back .brand {
    position: absolute;
    right: 28px; top: 26px;
    gap: 10px;
  }
  .card--back .brand__mark { width: 22px; height: 22px; }
  .card--back .brand__name { font-size: 32px; }

  .person {
    position: absolute;
    left: 34px; top: 112px;
  }
  .person__name { font-size: 19px; font-weight: 700; }
  .person__role { font-size: 13px; margin-top: 6px; color: var(--muted); }

  .contacts {
    position: absolute;
    left: 34px; top: 190px;
    list-style: none;
  }
  .contacts__item {
    display: flex;
    align-items: center;
    gap: 12px;
    font-size: 13.5px;
    font-weight: 500;
    line-height: 22px;
    color: var(--ink);
    white-space: nowrap;
  }
  .contacts__item svg { width: 14px; height: 14px; flex: none; fill: var(--lime); }
  .contacts__item--web { font-weight: 700; }
</style>
</head>
<body>

  <section class="card card--front" aria-label="Business card front">
    <div class="brand">
      <span class="brand__mark"></span>
      <span class="brand__name">Larchly</span>
    </div>
  </section>

  <section class="card card--back" aria-label="Business card back">
    <div class="brand">
      <span class="brand__mark"></span>
      <span class="brand__name">Larchly</span>
    </div>

    <div class="person">
      <p class="person__name">Trevor Halse</p>
      <p class="person__role">Director</p>
    </div>

    <ul class="contacts">
      <li class="contacts__item">
        <svg viewBox="0 0 14 14" aria-hidden="true"><path d="M7 0a5 5 0 0 1 5 5c0 3.5-5 9-5 9S2 8.5 2 5a5 5 0 0 1 5-5zm0 3a2 2 0 1 0 0 4 2 2 0 0 0 0-4z"/></svg>
        27A Pemberly Lane, Brackenvale VIC 3999 Australia
      </li>
      <li class="contacts__item">
        <svg viewBox="0 0 14 14" aria-hidden="true"><path d="M4 0h6a1 1 0 0 1 1 1v12a1 1 0 0 1-1 1H4a1 1 0 0 1-1-1V1a1 1 0 0 1 1-1zm0 2v9h6V2zm3 10a.8.8 0 1 0 0 1.6.8.8 0 0 0 0-1.6z"/></svg>
        +61 417 352 940
      </li>
      <li class="contacts__item">
        <svg viewBox="0 0 14 14" aria-hidden="true"><path d="M3 1l2.5 3-1.3 1.4a8 8 0 0 0 4.4 4.4L10 8.5l3 2.5-1.6 2A10.5 10.5 0 0 1 1 2.6z"/></svg>
        1300 514 637
      </li>
      <li class="contacts__item">
        <svg viewBox="0 0 14 14" aria-hidden="true"><path d="M0 3h14v8H0zm1 .8v.4l6 4 6-4v-.4z"/></svg>
        trevor.halse@larchly-example.com.au
      </li>
      <li class="contacts__item contacts__item--web">
        <svg viewBox="0 0 14 14" aria-hidden="true"><path d="M7 0a7 7 0 1 1 0 14A7 7 0 0 1 7 0zM1.5 6.3h2.6A11 11 0 0 1 5.3 1.5a5.6 5.6 0 0 0-3.8 4.8zm4 0h3a9.5 9.5 0 0 0-1.5-4.7 9.5 9.5 0 0 0-1.5 4.7zm4.4 0h2.6a5.6 5.6 0 0 0-3.8-4.8 11 11 0 0 1 1.2 4.8zM1.5 7.7a5.6 5.6 0 0 0 3.8 4.8 11 11 0 0 1-1.2-4.8zm4 0a9.5 9.5 0 0 0 1.5 4.7 9.5 9.5 0 0 0 1.5-4.7zm4.4 0a11 11 0 0 1-1.2 4.8 5.6 5.6 0 0 0 3.8-4.8z"/></svg>
        www.larchly-example.com.au
      </li>
    </ul>
  </section>

</body>
</html>
```